Web Page Design for Major Airline Consolidator

We need a new design for an airline consolidator based out of NY. We'd really like to get the design as quickly as possible.

Here is a *very* rough mockup of what the site could look like, along with 3 main competitor's sites. Needless to say, they want a design that looks much better than their competitors. Please note that the mockup is an idea only, feel free to enhance / improve upon it.

Mockup - https://plenvora.com/trqbuild/KXMfoTzQ

Competitors:
- http://www.ruvelta.com/
- http://www.bindomark.com/home2.html
- https://www.lusopex.com/index.php
Updates

Project Deadline Extended
Reason: As per request from designers to submit additional designs.

Target Market(s)

target markets are identified in the mockup

Industry/Entity Type

Airline

Number of Pages Required

1 page

Requirements
Must have
• need space on the left side for a travel request form which is missing in the mockup. Form should have standard air booking fields (to, from, date arrival & departure, travel class, etc).

```html
<!DOCTYPE html>
<html lang="en">
<head>
<meta charset="utf-8">
<title>Harwick Tours</title>
<link href="https://fonts.googleapis.com/css2?family=Open+Sans:wght@400;600;700&display=swap" rel="stylesheet">
<style>
:root{
  --green:#0f5c3b;
  --green-dark:#0b4a2f;
  --blue:#35a2d8;
  --ink:#222;
  --muted:#555;
  --line:#d8d8d8;
  --panel:#f4f4f4;
}
*{box-sizing:border-box;margin:0;padding:0}
html,body{width:680px;height:1200px;overflow:hidden;background:#fff}
body{position:relative;font-family:"Open Sans",sans-serif;color:var(--ink)}
.abs{position:absolute}
.topbar{left:353px;top:0;width:327px;height:16px;background:#111;color:#fff;font-size:6px;display:flex;align-items:center;padding-left:26px;gap:8px}
.topbar .search{margin-left:70px;width:56px;height:7px;border:1px solid #aaa;border-radius:2px}
.topbar .lang{margin-left:46px}
.brand{left:64px;top:18px;display:flex;align-items:center;gap:6px}
.brand .mark{width:34px;height:34px;background:#777}
.brand .name{font-size:22px;font-weight:400;color:#555;line-height:1}
.brand .tag{font-size:7px;color:#555}
.contact{top:36px;font-size:11px;color:#555;display:flex;align-items:center;gap:8px}
.nav{left:64px;top:74px;width:552px;height:22px;border-top:1px solid #999;border-bottom:1px solid #999;display:flex;justify-content:space-between;align-items:center;font-size:7.5px;color:#333}
.hero{left:0;top:102px;width:680px;height:448px;background:linear-gradient(90deg,#7a4a2e,#b67e5a 30%,#8d6d62 60%,#5a3f38)}
.quote{left:64px;top:120px;width:171px;height:238px;background:var(--green);border-radius:3px;padding:20px 14px;color:#fff}
.quote h2{background:#fff;color:#222;font-weight:400;font-size:14px;text-align:center;padding:5px 0;margin:0 6px 14px}
.quote .row{display:flex;justify-content:space-between;align-items:center;font-size:10px;font-weight:600;height:23.5px}
.quote .field{background:#fff;height:14px;border-radius:2px}
.quote .btn{display:block;margin:10px auto 0;width:64px;background:#fff;color:#222;font-size:10px;text-align:center;padding:2px 0;border-radius:2px}
.heroimg{left:246px;top:120px;width:370px;height:240px;background:linear-gradient(120deg,#5d6c78,#c9cfd4 55%,#e8e2d8)}
.heroinfo{left:246px;top:141px;width:162px;height:131px;background:rgba(20,20,20,.85);color:#fff;padding:8px 10px}
.heroinfo h3{font-size:12px;font-weight:600;text-align:center;line-height:1.3;margin-bottom:6px}
.heroinfo li{list-style:none;font-size:7px;line-height:1.35;margin-bottom:4px;padding-left:11px;position:relative}
.heroinfo li:before{content:"✔";position:absolute;left:0}
.cards{left:64px;top:367px;width:552px;height:183px;background:#fff;border-radius:4px}
.card{top:21px;width:174px;height:158px;background:var(--panel);border:2px solid var(--green);border-radius:6px;padding:10px 12px}
.card h4{font-size:10.5px;font-weight:400;text-align:center;border-bottom:1px solid #333;padding-bottom:3px}
.card .sub{font-size:6px;text-align:center;color:#444;margin:8px 0 10px}
.card .body{display:flex;gap:4px;font-size:6px;line-height:1.55;color:#444}
.card .pic{flex:0 0 70px;height:47px;background:linear-gradient(#8fb3d0,#6e8c4a)}
.card .join{display:block;margin:15px auto 0;width:66px;background:var(--green);color:#fff;font-size:6.5px;font-weight:600;text-align:center;padding:4px 0;border-radius:2px}
.corp-img{left:74px;top:576px;width:211px;height:142px;border:2px solid #666;background:linear-gradient(90deg,#8a8f93,#d6d8da 60%,#b9c3cc)}
.corp{left:313px;top:572px;width:310px;font-size:10px;color:#333;line-height:1.2}
.corp h3{font-size:12px;font-weight:400;margin-bottom:18px}
.corp p{margin-bottom:7px}
.corp .cta{display:inline-block;margin-top:10px;background:var(--green);color:#fff;padding:4px 9px;font-size:10px}
.band{left:0;top:748px;width:680px;height:186px;background:var(--blue);color:#fff}
.notch{width:0;height:0;border-left:10px solid transparent;border-right:10px solid transparent}
.band h2{position:absolute;top:24px;width:100%;text-align:center;font-size:15px;font-weight:600}
.group-img{top:65px;width:147px;height:97px}
.group{top:71px;width:105px;font-size:6px;line-height:1.6}
.group h4{font-size:8px;font-weight:700;margin-bottom:4px}
.group .cta{display:inline-block;margin-top:10px;background:var(--green);padding:3px 6px;font-size:6.5px}
.person{left:65px;top:952px;width:140px;height:141px;background:linear-gradient(#b8956a,#4a4a52)}
.motto{left:218px;top:956px;width:400px;font-size:14px;line-height:1.35;color:#333}
.info{top:1030px;width:105px;height:64px;border:2px solid var(--green);padding:3px 6px;font-size:5.5px;line-height:1.7;color:#666}
.info h5{font-size:8px;font-weight:400;color:#444}
.trusted{left:102px;top:1125px;font-size:14px;color:#333}
.badge{top:1118px;background:#bbb;border-radius:2px}
.footer{left:0;top:1172px;width:680px;height:28px;background:var(--green);color:#fff;font-size:9px;display:flex;align-items:center;padding-left:66px}
.social{top:1177px;width:18px;height:18px;border-radius:50%;background:#111}
</style>
</head>
<body>
<div class="abs topbar"><span>Log in</span><span>|</span><span>Register</span><span class="search"></span><span class="lang">EN ▾</span></div>

<div class="abs brand">
  <div class="mark"></div>
  <div><div class="name">Harwick Tours</div><div class="tag">The Professional's choice since 1974</div></div>
</div>
<div class="abs contact" style="left:353px">
  <svg width="14" height="10" viewBox="0 0 14 10"><rect width="14" height="10" fill="#0f5c3b"/><path d="M0 0l7 5 7-5" stroke="#fff" fill="none"/></svg>info@harwicktours.com
</div>
<div class="abs contact" style="left:529px">
  <svg width="12" height="12" viewBox="0 0 12 12"><rect width="12" height="12" rx="2" fill="#0f5c3b"/><path d="M4 3c0 3 2 6 5 6" stroke="#fff" stroke-width="1.6" fill="none"/></svg>888-555-0172
</div>

<nav class="abs nav"><span>Home</span><span>Travel Agencies</span><span>Religious &amp; Group Travel</span><span>Corporate Concierge</span><span>Niche Agencies</span><span>Destinations</span><span>About Harwick</span><span>Restricted Area</span></nav>

<div class="abs hero" role="img" aria-label="Hot air balloons drifting in a sunset sky"></div>

<form class="abs quote">
  <h2>Get a Quote</h2>
  <div class="row">Name<span class="field" style="width:87px"></span></div>
  <div class="row">Email<span class="field" style="width:87px"></span></div>
  <div class="row">Depart from<span class="field" style="width:62px"></span></div>
  <div class="row">Arrive at<span class="field" style="width:62px"></span></div>
  <div class="row">Departure date<span class="field" style="width:46px"></span></div>
  <div class="row">Return date<span class="field" style="width:46px"></span></div>
  <span class="btn">Submit</span>
</form>

<div class="abs heroimg" role="img" aria-label="Smiling travel agent at her desk in front of a world map"></div>
<div class="abs heroinfo">
  <h3>More Than Just<br>Airline Consolidation</h3>
  <ul>
    <li>We're here for our clients!</li>
    <li>Over 40 years in business</li>
    <li>Locations across the USA</li>
    <li>50+ air carriers</li>
    <li>Worldwide + Europe &amp; Middle East travel</li>
  </ul>
</div>

<section class="abs cards">
  <div class="abs card" style="left:8px">
    <h4>Home Based Travel Agents</h4>
    <p class="sub">Find your way to financial freedom!</p>
    <div class="body"><p>•Don't lose another client to the big guys<br>•Get more referrals and more customers!<br>•Earn more per</p><div class="pic" role="img" aria-label="Suburban house with a green lawn"></div></div>
    <span class="join">Join Now</span>
  </div>
  <div class="abs card" style="left:189px">
    <h4>Small Travel Agencies</h4>
    <p class="sub">Accelerate your growth!</p>
    <div class="body"><p>•Don't lose another client to the big guys<br>•Get more referrals and more customers!<br>•Earn more per</p><div class="pic" role="img" aria-label="Suburban house with a green lawn"></div></div>
    <span class="join">Join Now</span>
  </div>
  <div class="abs card" style="left:371px">
    <h4>Corporate Travel Agencies</h4>
    <p class="sub">Earn &amp; retain higher value clients</p>
    <div class="body"><p>•Don't lose another client to the big guys<br>•Get more referrals and more customers!<br>•Earn more per</p><div class="pic" role="img" aria-label="Suburban house with a green lawn"></div></div>
    <span class="join">Join Now</span>
  </div>
</section>

<div class="abs corp-img" role="img" aria-label="Call center agents wearing headsets"></div>
<section class="abs corp">
  <h3>Airline Consolidators for Businesses &amp; Corporations</h3>
  <p>Tired of Travel Headaches? Make Business Travel EASY!</p>
  <p style="margin-bottom:0">•Excellent customer service, we staff over 200 agents and have locations in 6 major US cities<br>•Always available ...<br>buy in bulk &amp; save even more!<br>•Save more by going direct to the consolidator!<br>•Your best interests are ours!</p>
  <span class="cta">Experience the difference of Harwick!</span>
</section>

<section class="abs band">
  <div class="abs notch" style="left:330px;top:0;border-top:10px solid #fff"></div>
  <h2>Group Travel - Missionary Airfares, HAJJ &amp; Umra Discounted Airfares</h2>
  <div class="abs group-img" style="left:64px;background:linear-gradient(#7f8a5e,#3b3a3a)" role="img" aria-label="Smiling family group"></div>
  <div class="abs group" style="left:222px">
    <h4>HAJJ Group Travel Rates</h4>
    <p>Lorem ipsum dolor sit amet, consectetur adipisicing elit, sed do eiusmod tempor incididunt ut labore et dolore magna aliqua. Ut enim ad minim.</p>
    <span class="cta">Contact Us Now</span>
  </div>
  <div class="abs group-img" style="left:354px;background:linear-gradient(#6d8a3c,#a88a6a)" role="img" aria-label="Missionary with children on a country path"></div>
  <div class="abs group" style="left:513px">
    <h4>Missionary Travel</h4>
    <p>Lorem ipsum dolor sit amet, consectetur adipisicing elit, sed do eiusmod tempor incididunt ut labore et dolore magna aliqua. Ut enim ad minim.</p>
    <span class="cta">Contact Us Now</span>
  </div>
  <div class="abs notch" style="left:330px;bottom:-10px;border-top:10px solid var(--blue)"></div>
</section>

<div class="abs person" role="img" aria-label="Portrait of a smiling businessman"></div>
<p class="abs motto">"Great airfares are only the beginning, exceptional customer service and caring for our clients is what makes us so unique"</p>
<div class="abs info" style="left:232px"><h5>Our History</h5>Lorem ipsum dolor sit ame consectetur adipisicing elit sed do eiusmod tempor incididunt ut labore et.</div>
<div class="abs info" style="left:364px"><h5>Our Divisions</h5>Lorem ipsum dolor sit ame consectetur adipisicing elit sed do eiusmod tempor incididunt ut labore et.</div>
<div class="abs info" style="left:495px"><h5>Our Employees</h5>Lorem ipsum dolor sit ame consectetur adipisicing elit sed do eiusmod tempor incididunt ut labore et.</div>

<p class="abs trusted">Trusted Members of:</p>
<div class="abs badge" style="left:320px;width:58px;height:26px"></div>
<div class="abs badge" style="left:411px;width:36px;height:32px"></div>
<div class="abs badge" style="left:484px;width:48px;height:30px"></div>

<footer class="abs footer">Copyright©harwicktours.2014.All Rights Reserved</footer>
<span class="abs social" style="left:512px"></span>
<span class="abs social" style="left:540px"></span>
<span class="abs social" style="left:568px"></span>
<span class="abs social" style="left:596px"></span>
</body>
</html>
```